Fact/Marketing Sheet(s) for Health & Wellness Plan

We are wanting to market a new program that we have for Health & Wellness Benefits for our customer Kestrel Federation of Township Guilds (KFTG). We would like to present this information in a professional format that compels the recipient/reader to act on this.
I like the format of the TofB document (see attahed)- however would adjust the photo to be something Agricultural related.
I am very interested to see other ideas that may be proposed.
In addition to the content that we are wanting to communicate at this time (see attached (KFTG Project ) I have also included our Style Guide , logos, and pattern if needed.
Members of the Kestrel Federation of Township Guilds - typically business leaders and volunteers in communities across Alberta.
- In Brand Document

```html
<!DOCTYPE html>
<html lang="en">
<head>
<meta charset="utf-8">
<title>Health &amp; Wellness Benefits Fact Sheets</title>
<link href="https://fonts.googleapis.com/css2?family=Arimo:wght@400;700&family=Montserrat:wght@600;700&family=PT+Serif&display=swap" rel="stylesheet">
<style>
:root{
  --navy:#1f2a6b;
  --blue:#2c4fb0;
  --royal:#2e3fa3;
  --ink:#333;
  --stage:#1e1e1e;
  --grass1:#3f7a1c;
  --grass2:#9cc43a;
}
*{box-sizing:border-box;margin:0;padding:0}
html,body{width:906px;height:1200px;overflow:hidden;background:var(--stage)}
body{position:relative;font-family:Arimo,Arial,sans-serif;color:var(--ink)}
.page{position:absolute;width:410px;height:575px;background:linear-gradient(135deg,#fbfbfb,#e9e9e9);overflow:hidden}
.p1{left:43px;top:15px}.p2{left:453px;top:15px}
.p3{left:43px;top:610px}.p4{left:453px;top:610px}
.header{position:absolute;left:0;top:0;width:410px;height:170px}
.prepared-for{position:absolute;right:14px;top:12px;text-align:right;font-size:6px;color:var(--navy)}
.client-name{display:block;margin-top:3px;font-family:Montserrat,sans-serif;font-weight:700;font-size:6.5px;line-height:1.25;color:var(--navy);text-transform:uppercase}
.client-name::before{content:"";display:inline-block;width:9px;height:9px;border-radius:50%;background:var(--blue);vertical-align:middle;margin-right:4px}
.title{position:absolute;right:14px;font-family:"PT Serif",serif;font-size:17px;line-height:1.35;color:var(--navy);text-align:right}
.title.compact{font-size:15px}
.broker{position:absolute;left:16px;top:112px;color:#fff;font-size:5px;line-height:1.2}
.broker b{display:block;font-family:"PT Serif",serif;font-weight:400;font-size:11px;letter-spacing:.5px}
.broker .mark{position:absolute;left:0;top:4px;width:16px;height:16px;border:1.2px solid #fff;border-radius:50%}
.broker .txt{padding-left:22px}
.body{position:absolute;left:28px;right:28px;top:185px;font-size:7.5px;line-height:1.95}
.body.tight{line-height:1.75}
h2{font-family:Montserrat,sans-serif;font-weight:700;font-size:11px;color:var(--royal);margin:4px 0 2px}
ol{list-style:none}
.indent{padding-left:14px}
ul.bullets{padding-left:60px;list-style:disc}
.rule{height:2px;background:var(--royal);margin:10px 0 6px}
.apply{text-align:center;font-weight:700;font-size:7.5px}
.footnote{position:absolute;left:0;right:0;bottom:60px;text-align:center;font-size:4.5px;color:#555;z-index:2}
.grass{position:absolute;left:0;right:0;bottom:0;height:48px;background:linear-gradient(180deg,rgba(244,244,244,0),var(--grass2) 35%,var(--grass1))}
.highlights{display:grid;grid-template-columns:1fr 1fr;gap:10px 14px;margin:10px 0 0 20px;font-size:6.3px;line-height:1.4}
.hl{display:flex;align-items:center;gap:10px}
.hl svg{flex:none}
.cover-wrap{position:relative}
.shield{position:absolute;right:0;top:0}
.cards{display:flex;gap:14px;margin-top:24px;justify-content:center;align-items:flex-start}
.card{position:relative;width:80px;height:80px;border-radius:12px 12px 18px 18px;background:var(--blue);color:#fff;text-align:center;font-size:7px;line-height:1.4;padding-top:24px}
.card.dark{background:var(--navy)}
.card.low{margin-top:20px}
.card .num{position:absolute;left:50%;top:-18px;transform:translateX(-50%);width:36px;height:36px;border-radius:50%;background:var(--navy);border:2.5px solid #fff;font-family:Montserrat,sans-serif;font-weight:600;font-size:14px;line-height:31px}
.card b{display:block;letter-spacing:.4px}
.notice{text-align:center;font-family:Montserrat,sans-serif;font-weight:700;font-size:8px;color:var(--royal);line-height:1.9;margin-top:10px}
</style>
</head>
<body>

<svg width="0" height="0" style="position:absolute">
  <defs>
    <linearGradient id="soil" x1="0" y1="0" x2="1" y2="1"><stop offset="0" stop-color="#6f8f3a"/><stop offset=".5" stop-color="#5a4630"/><stop offset="1" stop-color="#2c241c"/></linearGradient>
    <linearGradient id="leaf" x1="0" y1="0" x2="1" y2="1"><stop offset="0" stop-color="#c7d98a"/><stop offset=".5" stop-color="#6f9b2e"/><stop offset="1" stop-color="#2f4f16"/></linearGradient>
    <linearGradient id="sprout" x1="0" y1="0" x2="0" y2="1"><stop offset="0" stop-color="#2b3d1a"/><stop offset=".6" stop-color="#6a8f3a"/><stop offset="1" stop-color="#3a2b20"/></linearGradient>
    <linearGradient id="sky" x1="0" y1="0" x2="0" y2="1"><stop offset="0" stop-color="#2f7fd6"/><stop offset=".5" stop-color="#bfe0f7"/><stop offset=".75" stop-color="#c5d84a"/><stop offset="1" stop-color="#4d8a23"/></linearGradient>
  </defs>
</svg>

<section class="page p1">
  <svg class="header" viewBox="0 0 410 170">
    <polygon points="0,0 105,0 215,150 0,150" fill="url(#soil)" role="img" aria-label="Photo of a young plant being watered in garden soil"/>
    <polygon points="125,0 140,0 250,150 235,150" fill="url(#soil)" role="img" aria-label="Continuation of the garden photo"/>
    <polygon points="0,105 145,105 172,150 0,150" fill="var(--navy)"/>
    <rect x="0" y="150" width="410" height="18" fill="var(--blue)"/>
  </svg>
  <div class="broker"><span class="mark"></span><div class="txt">Prepared By:<b>BIRCHGATE</b>BROKERS</div></div>
  <div class="prepared-for">Prepared For:<span class="client-name">Kestrel Federation of<br>Township Guilds</span></div>
  <div class="title compact" style="top:74px">Employee Family Assistance<br>Program &amp; Medical<br>Second Opinion</div>
  <div class="body">
    <h2>COVERAGE AVAILABLE FOR:</h2>
    <ol><li>1.)&nbsp; Employees</li><li>2.)&nbsp; Board Members</li><li>3.)&nbsp; Spouses and dependent children of employees or board members</li></ol>
    <ol style="margin-top:6px">
      <li>1.)&nbsp; Immediate and confidential access to variety of programs and services to help with work<br><span class="indent">and life issues before they become more serious.</span></li>
      <li>2.)&nbsp; Services include, but are not limited to:</li>
    </ol>
    <ul class="bullets"><li>Short Term Counseling</li><li>Legal Advice</li><li>Financial Planning</li><li>Nutritional Counseling</li><li>and much more</li></ul>
    <ol style="margin-top:12px"><li>3.)&nbsp; Medical Second Opinion provides an independent review of diagnoses and treatment<br><span class="indent">recommendations. These reviews are completed by medical professionals trained at some</span><br><span class="indent">of the top medical institutions in the world.</span></li></ol>
    <div class="rule" style="margin-top:14px"></div>
    <p class="apply">To apply, please contact us at (555) 014-2287 or benefits@birchgate.ca</p>
  </div>
  <p class="footnote">*Policies are subject to standard conditions and exclusions. Please refer to the specific policy wordings for complete details.</p>
  <div class="grass" role="img" aria-label="Photo of green grass along the page bottom"></div>
</section>

<section class="page p2">
  <svg class="header" viewBox="0 0 410 170">
    <polygon points="0,0 105,0 215,150 0,150" fill="url(#leaf)" role="img" aria-label="Photo of fresh green tea leaves"/>
    <polygon points="125,0 140,0 250,150 235,150" fill="url(#leaf)" role="img" aria-label="Continuation of the leaf photo"/>
    <polygon points="0,105 145,105 172,150 0,150" fill="var(--navy)"/>
    <rect x="0" y="150" width="410" height="18" fill="var(--blue)"/>
  </svg>
  <div class="broker"><span class="mark"></span><div class="txt">Prepared By:<b>BIRCHGATE</b>BROKERS</div></div>
  <div class="prepared-for">Prepared For:<span class="client-name">Kestrel Federation of<br>Township Guilds</span></div>
  <div class="title" style="top:95px">Health and Wellness<br>Benefits Program</div>
  <div class="body" style="line-height:1.7">
    <h2>PROGRAM HIGHLIGHTS</h2>
    <div class="rule" style="margin:2px 0 4px"></div>
    <p style="font-size:6.5px;line-height:1.35">Flexible coverage options with the ability to build your own plan that is best for your employees and board members.</p>
    <div class="highlights">
      <div class="hl"><svg width="24" height="26" viewBox="0 0 24 26"><path d="M12 1 L22 5 V12 C22 19 17 23 12 25 C7 23 2 19 2 12 V5 Z" fill="none" stroke="var(--royal)" stroke-width="2"/><path d="M7 13 L11 17 L17 9" fill="none" stroke="var(--royal)" stroke-width="2"/></svg><span>Added protection for your employees / board members and their families</span></div>
      <div class="hl"><svg width="24" height="26" viewBox="0 0 24 26"><circle cx="12" cy="10" r="8" fill="none" stroke="var(--royal)" stroke-width="2"/><circle cx="12" cy="10" r="4" fill="var(--royal)"/><path d="M7 16 L5 25 L9 22 L12 25 L15 22 L19 25 L17 16" fill="var(--royal)"/></svg><span>Guaranteed issue with<br>no medical underwriting</span></div>
      <div class="hl"><svg width="24" height="26" viewBox="0 0 24 26"><circle cx="14" cy="6" r="4" fill="var(--royal)"/><path d="M1 18 C6 14 10 15 14 17 L22 14 C23 16 22 18 20 19 L12 24 L1 22 Z" fill="var(--royal)"/></svg><span>Exclusive to existing members of the Kestrel Federation of Township Guilds</span></div>
      <div class="hl"><svg width="26" height="22" viewBox="0 0 26 22"><rect x="1" y="4" width="22" height="15" rx="2" fill="none" stroke="var(--royal)" stroke-width="2"/><rect x="1" y="8" width="22" height="3" fill="var(--royal)"/><rect x="14" y="14" width="6" height="2" fill="var(--royal)"/></svg><span>Simple and easy enrollment with convenient payment options</span></div>
    </div>
    <div class="rule" style="margin:14px 0 6px"></div>
    <p class="apply" style="line-height:1.8">To apply, please contact our broker partner, Birchgate Brokers<br>at (555) 014-2287 or benefits@birchgate.ca</p>
    <div class="cover-wrap">
      <h2 style="margin-top:8px">COVERAGES AVAILABLE</h2>
      <ol style="line-height:2">
        <li>1.)&nbsp; Health Spending Accounts / Taxable Wellness Accounts</li>
        <li>2.)&nbsp; Life &amp; Disability Insurance</li>
        <li>3.)&nbsp; Critical Illness</li>
        <li>4.)&nbsp; Employee &amp; Family Assistance Program</li>
        <li>5.)&nbsp; Medical Second Opinion</li>
        <li>6.)&nbsp; Accidental Death and Dismemberment</li>
        <li>7.)&nbsp; Hospital Cash</li>
        <li>8.)&nbsp; Final Expenses</li>
      </ol>
      <svg class="shield" width="100" height="122" viewBox="0 0 100 122" role="img" aria-label="Shield-shaped photo of colourful umbrellas floating in a blue sky">
        <defs><linearGradient id="umb" x1="0" y1="0" x2="1" y2="1"><stop offset="0" stop-color="#e39a3a"/><stop offset=".45" stop-color="#cfe2f3"/><stop offset=".8" stop-color="#3a7fd0"/><stop offset="1" stop-color="#d33"/></linearGradient></defs>
        <path d="M4 6 L96 6 V60 C96 92 70 110 50 118 C30 110 4 92 4 60 Z" fill="url(#umb)" stroke="#fff" stroke-width="3"/>
      </svg>
    </div>
  </div>
  <p class="footnote">*Policies are subject to standard conditions and exclusions. Please refer to the specific policy wordings for complete details.</p>
  <div class="grass" role="img" aria-label="Photo of green grass along the page bottom"></div>
</section>

<section class="page p3">
  <svg class="header" viewBox="0 0 410 170">
    <polygon points="0,0 105,0 215,150 0,150" fill="url(#sprout)" role="img" aria-label="Photo of a young seedling growing from dark soil"/>
    <polygon points="125,0 140,0 250,150 235,150" fill="url(#sprout)" role="img" aria-label="Continuation of the seedling photo"/>
    <polygon points="0,105 145,105 172,150 0,150" fill="var(--navy)"/>
    <rect x="0" y="150" width="410" height="18" fill="var(--blue)"/>
  </svg>
  <div class="broker"><span class="mark"></span><div class="txt">Prepared By:<b>BIRCHGATE</b>BROKERS</div></div>
  <div class="prepared-for">Prepared For:<span class="client-name">Kestrel Federation of<br>Township Guilds</span></div>
  <div class="title" style="top:72px">Critical Illness Final<br>Expense AD&amp;D<br>Hospital Cash</div>
  <div class="body tight">
    <h2>COVERAGE AVAILABLE UP TO AGE 70 FOR:</h2>
    <ol><li>1.)&nbsp; Employees</li><li>2.)&nbsp; Board Members</li><li>3.)&nbsp; Spouses and dependent children of employees or board members</li></ol>
    <h2 style="margin-top:8px">COVERAGE HIGHLIGHTS:</h2>
    <ol>
      <li>1.)&nbsp; Simple and quick application process</li>
      <li>2.)&nbsp; Portable coverage that the employee/board member can take with them if they leave<br><span class="indent">their employer</span></li>
      <li>3.)&nbsp; 24/7 protection whether you are working, at home, or travelling</li>
      <li>4.)&nbsp; 23 covered critical illness conditions including heart attack, stroke and cancer</li>
    </ol>
    <div class="rule" style="margin:6px 0 5px"></div>
    <p class="apply">For a quote, please contact us at (555) 014-2287 or benefits@birchgate.ca</p>
    <div class="cards">
      <div class="card dark"><span class="num">01</span><b>Critical Illness</b>(Up to $150,000)<br><b>$25,000<br>Guaranteed</b></div>
      <div class="card low"><span class="num">02</span><b>Final Expense</b>(Up to $25,000)</div>
      <div class="card dark"><span class="num">03</span>Accidental Death<br>&amp;<br>Dismemberment<br>(Up to $500,000)</div>
      <div class="card low"><span class="num">04</span><b>Hospital Cash</b>(Up to $250 / Day)</div>
    </div>
  </div>
  <p class="footnote">*Policies are subject to standard conditions and exclusions. Please refer to the specific policy wordings for complete details.</p>
  <div class="grass" role="img" aria-label="Photo of green grass along the page bottom"></div>
</section>

<section class="page p4">
  <svg class="header" viewBox="0 0 410 170">
    <polygon points="0,0 105,0 215,150 0,150" fill="url(#sky)" role="img" aria-label="Photo of a sunny sky over a green and yellow crop field"/>
    <polygon points="125,0 140,0 250,150 235,150" fill="url(#sky)" role="img" aria-label="Continuation of the field photo"/>
    <polygon points="0,105 145,105 172,150 0,150" fill="var(--navy)"/>
    <rect x="0" y="150" width="410" height="18" fill="var(--blue)"/>
  </svg>
  <div class="broker"><span class="mark"></span><div class="txt">Prepared By:<b>BIRCHGATE</b>BROKERS</div></div>
  <div class="prepared-for">Prepared For:<span class="client-name">Kestrel Federation of<br>Township Guilds</span></div>
  <div class="title" style="top:95px">Health Care &amp; Wellness<br>Spending Accounts</div>
  <div class="body">
    <h2>NO START UP FEES</h2>
    <ol>
      <li>1.) A health care spending account offers comprehensive health &amp; dental benefits while giving<br><span class="indent">your employees the flexibility to choose how they spend their health care dollars.</span></li>
      <li>2.) Taxable wellness accounts provide employees with the means to proactively manage their<br><span class="indent">physical, mental and financial well-being. Gym memberships, vitamins and supplements,</span><br><span class="indent">and many other wellness expenses are available under this benefit.</span></li>
      <li>3.) Travel insurance can be provided for your employees in addition to your health spending<br><span class="indent">account.</span></li>
      <li>4.) Virtual health care can be added by the employee to their plan for them and their family.</li>
      <li>5.) Traditional group benefit plans are available which include life and disability insurance.<br><span class="indent">Available to employers with 3 or more employees.</span></li>
    </ol>
    <p class="notice">COVERAGE IS AVAILABLE TO T4'D EMPLOYEES ONLY AND<br>THEIR FAMILIES.</p>
    <div class="rule" style="margin-top:4px"></div>
    <p class="apply">To apply, please contact us at (555) 014-2287 or benefits@birchgate.ca</p>
  </div>
  <p class="footnote">*Policies are subject to standard conditions and exclusions. Please refer to the specific policy wordings for complete details.</p>
  <div class="grass" role="img" aria-label="Photo of green grass along the page bottom"></div>
</section>

</body>
</html>
```